PLOVEN Business Card

Coastal Build Additions and Refits. I need a business card designed for this new high end renovation business. I would like the logo centered on the back side with the ABN (37 915 402 176) on the bottom right hand corner.

I would like the following information placed on the other side along with some customized pattern or design.

Derek Collwood
Director
Phone: 1300 480 957
Fax: (02) 8145 9021
Website: www.plovenbuilders.com.au
Email: d.collwood@plovenbuilders.com.au
PO Box 87,
Kelvinbrook NSW 2069

(FB Logo) PLOVEN - Coastal Build Additions and Refits

The final design should communicate professionalism and trust.

Back side background colour: white
Front side: Undecided

```html
<!DOCTYPE html>
<html lang="en">
<head>
<meta charset="utf-8">
<title>PLOVEN Business Card</title>
<link rel="stylesheet" href="https://fonts.googleapis.com/css2?family=Open+Sans:ital,wght@0,400;0,600;1,400;1,600&display=swap">
<style>
  :root {
    --backdrop: #c2bbb3;
    --brand-blue: #1f6ea8;
    --brand-blue-light: #3a86bd;
    --ink-blue: #2f6fa6;
    --ink-grey: #6b6b6b;
    --ink-dark: #3a3a3a;
    --paper: #ffffff;
    --rule: #8fb0cc;
  }
  * { margin: 0; padding: 0; box-sizing: border-box; }
  html, body { width: 1200px; height: 800px; overflow: hidden; }
  body {
    background: var(--backdrop);
    font-family: "Open Sans", Arial, sans-serif;
    display: flex;
    align-items: center;
    justify-content: center;
    gap: 40px;
  }
  .card {
    position: relative;
    width: 520px;
    height: 300px;
    overflow: hidden;
    box-shadow: 0 10px 24px rgba(60, 50, 40, 0.25);
  }

  /* Front: blue */
  .card--front { background: var(--brand-blue); color: var(--paper); }
  .front-lines {
    position: absolute;
    inset: 0;
    width: 100%;
    height: 100%;
  }
  .front-lines line { stroke: var(--brand-blue-light); stroke-width: 1; }
  .front-brand {
    position: absolute;
    right: 40px;
    bottom: 44px;
    text-align: right;
  }
  .front-brand__name {
    font-size: 54px;
    font-weight: 600;
    letter-spacing: 2px;
    line-height: 1;
  }
  .front-brand__web {
    margin-top: 10px;
    font-size: 13px;
    letter-spacing: 1.5px;
  }

  /* Back: white */
  .card--back { background: var(--paper); }
  .back-brand {
    position: absolute;
    top: 28px;
    left: 0;
    right: 0;
    text-align: center;
  }
  .back-brand__name {
    font-size: 38px;
    font-weight: 600;
    letter-spacing: 3px;
    line-height: 1;
    color: var(--ink-blue);
  }
  .back-brand__tagline {
    margin-top: 6px;
    font-size: 9px;
    letter-spacing: 1.6px;
    text-transform: uppercase;
    color: var(--ink-dark);
  }
  .back-brand__rule {
    margin: 7px auto 0;
    width: 260px;
    height: 1px;
    background: var(--rule);
  }
  .contact {
    position: absolute;
    left: 32px;
    bottom: 22px;
    font-size: 9.5px;
    line-height: 1.7;
    color: var(--ink-grey);
  }
  .contact__label { color: var(--ink-blue); }
  .person {
    position: absolute;
    right: 36px;
    top: 118px;
    text-align: right;
  }
  .person__name {
    font-size: 17px;
    font-style: italic;
    font-weight: 600;
    color: var(--ink-blue);
    line-height: 1.3;
  }
  .person__role {
    font-size: 13px;
    color: var(--ink-dark);
  }
  .company-stack {
    position: absolute;
    right: 36px;
    top: 178px;
    text-align: right;
    font-size: 13px;
    line-height: 1.15;
    text-transform: uppercase;
    letter-spacing: 0.5px;
  }
  .company-stack__name { color: var(--ink-dark); }
  .company-stack__line--grey { color: var(--ink-grey); }
  .company-stack__line--blue { color: var(--ink-blue); }
  .abn {
    position: absolute;
    right: 36px;
    bottom: 14px;
    font-size: 8.5px;
    letter-spacing: 0.8px;
    color: var(--ink-grey);
  }
</style>
</head>
<body>
  <section class="card card--front" aria-label="Card front">
    <svg class="front-lines" viewBox="0 0 520 300" aria-hidden="true">
      <line x1="-20" y1="90" x2="200" y2="-20"/>
      <line x1="-20" y1="120" x2="240" y2="-20"/>
      <line x1="-20" y1="150" x2="280" y2="-20"/>
    </svg>
    <div class="front-brand">
      <div class="front-brand__name">PLOVEN</div>
      <div class="front-brand__web">www.plovenbuilders.com.au</div>
    </div>
  </section>

  <section class="card card--back" aria-label="Card back">
    <div class="back-brand">
      <div class="back-brand__name">PLOVEN</div>
      <div class="back-brand__tagline">Coastal Build Additions &amp; Refits</div>
      <div class="back-brand__rule"></div>
    </div>
    <div class="contact">
      <p><span class="contact__label">P</span> 1300 480 957</p>
      <p><span class="contact__label">F</span> (02) 8145 9021</p>
      <p><span class="contact__label">E</span> d.collwood@plovenbuilders.com.au</p>
      <p><span class="contact__label">W</span> www.plovenbuilders.com.au</p>
      <p>PO Box 87,</p>
      <p>Kelvinbrook NSW 2069</p>
    </div>
    <div class="person">
      <div class="person__name">Derek Collwood</div>
      <div class="person__role">director</div>
    </div>
    <div class="company-stack">
      <div class="company-stack__name">Ploven</div>
      <div class="company-stack__line--grey">Coastal Build</div>
      <div class="company-stack__line--blue">Additions</div>
      <div class="company-stack__line--blue">Refits</div>
    </div>
    <div class="abn">ABN 37 915 402 176</div>
  </section>
</body>
</html>
```